Broschüre für Immobilienvertrieb
Zielgruppe
Wir sind ein Immobilienvertrieb im Bereich Neubau-Immobilien und Bestand-Immobilien aus München. Die Firma BLOR existiert seit über 30 Jahren. Vor 4 Jahren haben wir ein cooles modernes Rebranding durchgeführt, sodass man mit unserem neuen Corporate Design richtig Spaß am Gestalten haben kann.
Eine konkrete Zielgruppe zu definieren ist schwierig, da unsere Käufer von 20-80 Jahren sein können. Ob junge, erfolgreiche Menschen, junge Familien, ältere Erwachsene, die von sich nach Auszug ihrer Kinder von ihrem Haus trennen wollen und eine kleinere Wohnung suchen oder einfach der Kapitalanleger, der auf der Suche nach einer neuen Investition ist.
Unsere CI ist gradlinig und setzt sich aus anthrazit, neonorange und weiß zusammen (Styleguide ist anbei).
Im Bestand gibt es nicht pro Objekt ein CI, hier wird mit dem der BLOR gearbeitet. Im Neubau hat jedes einzelne Projekt sein eigenes CI (siehe aktuell hausfeld-neu.de).
www.blor.de
Aufgabenstellung
Zur Aufgabe: Für die Bestandimmobilien benötigen wir ein neues Layout eines Immobilienexposé. Das Exposé wird sowohl online verwendet als auch von uns selbst gedruckt und gebunden.
Input: beigefügt ein Beispielexposé - grundsätzlich gefällt uns das Design, wir möchten jedoch etwas NEUES, modernes. Bitte keine Kopien des alten Exposés, dies soll nur als Input dienen (gerne können die Daten der Wohnung für den neuen Designentwurf genutzt werden).
Die Datei soll von uns befüllbar sein, sodass wir Texte und Bilder selbst austauschen können.
Für die Onlinenutzung gerne als doppelseitige Datei, zum Beispiel um Bilder über zwei Seiten größer und schöner darstellen zu können (Auszug Beispielimmobilie anbei). Für den Druck wird die Datei zudem mit Einzelseiten benötigt.

```html
<!DOCTYPE html>
<html lang="de">
<head>
<meta charset="utf-8">
<title>BLOR Exposé – Inhalt</title>
<link rel="stylesheet" href="https://fonts.googleapis.com/css2?family=Archivo+Black&family=Montserrat:wght@300;400;500;700&display=swap">
<style>
  :root {
    --backdrop: #dfe0e2;
    --paper: #efefef;
    --anthracite: #232323;
    --accent: #d63a22;
    --accent-line: #c9623f;
    --rule-brown: #9a5a3a;
    --sky-top: #15264d;
    --sky-mid: #2d5a9a;
    --sky-low: #7eb1de;
    --facade: #f2f3f5;
    --street: #7a8494;
    --white: #ffffff;
  }
  * { box-sizing: border-box; margin: 0; padding: 0; }
  html, body { width: 1200px; height: 1200px; overflow: hidden; }
  body {
    background: var(--backdrop);
    font-family: "Montserrat", sans-serif;
    color: var(--anthracite);
  }
  .spread {
    position: absolute;
    left: 60px; top: 218px;
    width: 1080px; height: 764px;
    display: flex;
    box-shadow: 0 18px 40px rgba(0,0,0,0.12);
  }
  .page { position: relative; width: 540px; height: 764px; overflow: hidden; }

  /* Left page: cover photo */
  .cover-photo {
    position: absolute; inset: 0;
    background:
      linear-gradient(180deg, var(--sky-top) 0%, var(--sky-mid) 35%, var(--sky-low) 58%, var(--facade) 66%, #dfe3ea 84%, var(--street) 92%, #5e6878 100%);
  }
  .brand {
    position: absolute;
    left: 150px; top: 300px;
    display: flex; align-items: center; gap: 18px;
    color: var(--white);
  }
  .brand-square {
    width: 26px; height: 26px;
    border: 4px solid var(--white);
  }
  .brand-name {
    font-family: "Montserrat", sans-serif;
    font-weight: 500;
    font-size: 72px;
    letter-spacing: 10px;
    line-height: 1;
  }

  /* Right page: contents */
  .contents { background: var(--paper); }
  .section-tag {
    position: absolute; right: 48px; top: 40px;
    width: 70px;
    font-family: "Archivo Black", sans-serif;
    font-size: 10px; letter-spacing: 1px;
    padding-bottom: 6px;
    border-bottom: 1px solid var(--accent-line);
  }
  .margin-rule {
    position: absolute; right: 62px; top: 80px;
    width: 1px; height: 540px;
    background: var(--accent-line);
  }
  .margin-marker {
    position: absolute; right: 56px; top: 118px;
    width: 13px; height: 62px;
    background: var(--accent);
  }
  .page-title { position: absolute; left: 76px; top: 170px; line-height: 1.1; }
  .page-title .strong {
    display: block;
    font-family: "Archivo Black", sans-serif;
    font-size: 40px; letter-spacing: 3px;
  }
  .page-title .light {
    display: block;
    font-weight: 300;
    font-size: 42px; letter-spacing: 4px;
  }
  .lettering-placeholder {
    position: absolute; left: 150px; top: 470px;
    width: 390px; height: 290px;
    background: linear-gradient(160deg, rgba(0,0,0,0.025), rgba(0,0,0,0.045));
  }
  .toc { position: absolute; left: 100px; top: 360px; list-style: none; }
  .toc-item { display: flex; align-items: flex-start; gap: 10px; margin-bottom: 30px; }
  .toc-item:nth-child(2) { margin-left: 16px; }
  .toc-item:nth-child(3) { margin-left: 32px; }
  .toc-number {
    font-family: "Archivo Black", sans-serif;
    font-size: 50px; line-height: 0.9;
    padding-top: 10px;
  }
  .toc-heading {
    font-family: "Archivo Black", sans-serif;
    font-size: 12px; letter-spacing: 1px;
    width: 118px;
    padding-bottom: 2px;
    border-bottom: 1px solid var(--rule-brown);
  }
  .toc-text {
    font-size: 10px; letter-spacing: 1px; line-height: 1.35;
    margin-top: 3px;
  }
  .folio {
    position: absolute; right: 40px; bottom: 96px;
    width: 82px;
    font-size: 9px; letter-spacing: 1.5px;
    padding-top: 6px;
    border-top: 1px solid var(--accent-line);
  }
  .folio b { font-family: "Archivo Black", sans-serif; font-weight: 400; }
  .gutter-shade {
    position: absolute; top: 0; left: 0; width: 30px; height: 100%;
    background: linear-gradient(90deg, rgba(0,0,0,0.06), rgba(0,0,0,0));
  }
</style>
</head>
<body>
  <main class="spread">
    <section class="page cover">
      <div class="cover-photo" role="img" aria-label="Foto: moderne weiße Wohnanlage unter blauem Himmel, Straße mit parkenden Autos"></div>
      <div class="brand">
        <span class="brand-square"></span>
        <span class="brand-name">BLOR</span>
      </div>
    </section>

    <section class="page contents">
      <div class="gutter-shade"></div>
      <div class="lettering-placeholder" role="img" aria-label="Dekorativer, blasser Pinselschriftzug im Hintergrund"></div>
      <div class="section-tag">Inhalt</div>
      <div class="margin-rule"></div>
      <div class="margin-marker"></div>

      <h1 class="page-title">
        <span class="strong">HIER STEHT</span>
        <span class="light">TITEL</span>
      </h1>

      <ol class="toc">
        <li class="toc-item">
          <span class="toc-number">04</span>
          <div>
            <div class="toc-heading">Inhalt</div>
            <p class="toc-text">Lorem ipsum dolor sit amet, conse<br>ctetuer adipiscing elit, sed diam</p>
          </div>
        </li>
        <li class="toc-item">
          <span class="toc-number">06</span>
          <div>
            <div class="toc-heading">Inhalt</div>
            <p class="toc-text">Lorem ipsum dolor sit amet, conse<br>ctetuer adipiscing elit, sed diam</p>
          </div>
        </li>
        <li class="toc-item">
          <span class="toc-number">08</span>
          <div>
            <div class="toc-heading">Inhalt</div>
            <p class="toc-text">Lorem ipsum dolor sit amet, conse<br>ctetuer adipiscing elit, sed diam</p>
          </div>
        </li>
      </ol>

      <div class="folio">Seite: <b>04</b></div>
    </section>
  </main>
</body>
</html>
```